Rosita Poster

We need a poster for the upcoming production of Opera Rosita. We want a modern looking avant garde poster with some traditional ellemnts. opera will be stage "out of the period" which means that there will be NO indication of time period or location. Colors for the set design are white and dark burgundy. some traditional Spanish elements will be used, particularly in the female costumes.

Target Market(s)

Arts community in Hartford and central CT

Requirements
Must have
• Logos of opera and orchestra.
• DUVAL ROSITA
• Rosita:
• Velda Rose Marsh
• Don Alvar:
• Bartholomew Fenwick
• Leandro:
• Dorian Webb
• Inésa:
• Annelise Krov,
• Joan Pettigrew
• Stage Director, Conductor
• Marcus Tolvane
• Chorus Master
• Lena Whitmoor
• www.pinebrookvocal.org
• www.thesilvestri.org
• (860) 472-6081
• Fri. November 9 / 7:30 pm / New Britain
• Harrow-By-Elm (47 Birch Rd)
• Sun. November 11 / 4 pm / New London
• Ossel Arts Center (718 Quill Ave)
• Sat. November 17 / 7:30 / Middletown
• RQT Performing Arts Center (514 Pellam Ct)
• Sun. November 18 / 2 pm / Hartford
• Fairbrook Lyceum Museum of Art (283 Cedar Way)
Should not have
• NOTE. Please see the graphics as suggestions. you an use other , you don't have to use all the graphics.

```html
<!DOCTYPE html>
<html lang="en">
<head>
<meta charset="utf-8">
<title>Duval Rosita Poster</title>
<link rel="stylesheet" href="https://fonts.googleapis.com/css2?family=Anton&family=Questrial&display=swap">
<style>
  :root {
    --stage-red: #d3121f;
    --night-black: #1a1617;
    --paper-white: #ffffff;
    --backdrop: #e9e6e2;
  }
  html, body {
    margin: 0;
    width: 1200px;
    height: 1200px;
    overflow: hidden;
    background: var(--backdrop);
  }
  .poster {
    position: absolute;
    left: 177px;
    top: 20px;
    width: 846px;
    height: 1161px;
    background: var(--stage-red);
    overflow: hidden;
    font-family: "Questrial", "Century Gothic", sans-serif;
    color: var(--paper-white);
  }
  .figure-field {
    position: absolute;
    left: 0;
    top: 0;
    width: 846px;
    height: 1161px;
  }
  .title {
    position: absolute;
    left: 25px;
    margin: 0;
    font-family: "Anton", "Impact", sans-serif;
    font-weight: 400;
    font-size: 138px;
    line-height: 1;
    letter-spacing: 2px;
    color: var(--paper-white);
    transform: scaleX(1.12);
    transform-origin: left top;
    white-space: nowrap;
  }
  .title-composer { top: 22px; }
  .title-opera { top: 164px; z-index: 2; }
  .partner {
    position: absolute;
    top: 58px;
    font-size: 13px;
    line-height: 12px;
    font-weight: 700;
    color: var(--night-black);
    text-transform: uppercase;
    -webkit-text-stroke: 0.3px var(--night-black);
  }
  .partner-orchestra { left: 541px; width: 150px; }
  .partner-opera { left: 700px; width: 120px; text-align: center; font-weight: 400; -webkit-text-stroke: 0; font-size: 14px; line-height: 15px; }
  .vertical {
    position: absolute;
    left: 796px;
    writing-mode: vertical-rl;
    transform: rotate(180deg);
    font-size: 21px;
    letter-spacing: 0.5px;
    white-space: nowrap;
    -webkit-text-stroke: 0.6px var(--paper-white);
  }
  .web-opera { top: 221px; }
  .web-orchestra { top: 594px; }
  .phone { top: 943px; font-size: 22px; letter-spacing: 1px; }
  .credits {
    position: absolute;
    top: 719px;
    margin: 0;
    font-size: 18px;
    line-height: 23px;
    -webkit-text-stroke: 0.5px var(--paper-white);
  }
  .credits-cast { left: 31px; }
  .credits-team { left: 349px; }
  .credits .indent { padding-left: 84px; }
  .show {
    position: absolute;
    margin: 0;
    font-size: 18px;
    line-height: 26px;
  }
  .show-date {
    display: block;
    font-size: 28px;
    line-height: 32px;
    margin-bottom: 2px;
    transform: scaleX(0.92);
    transform-origin: left;
    -webkit-text-stroke: 0.7px var(--paper-white);
  }
  .show-a { left: 31px; top: 896px; }
  .show-b { left: 31px; top: 1003px; }
  .show-c { left: 349px; top: 896px; }
  .show-d { left: 349px; top: 1003px; }
</style>
</head>
<body>
  <main class="poster">
    <svg class="figure-field" viewBox="0 0 846 1161" role="img" aria-label="Silhouette of a woman in a flowing Spanish dress">
      <path fill="var(--night-black)" d="M0,650 C90,540 240,500 380,430 C470,385 540,300 600,250 C660,200 720,260 740,420 C760,540 800,560 846,560 L846,1161 L0,1161 Z"/>
    </svg>

    <h1 class="title title-composer">DUVAL</h1>
    <h1 class="title title-opera">ROSITA</h1>

    <div class="partner partner-orchestra">Silvestri<br>Chamber<br>Orchestra</div>
    <div class="partner partner-opera">Pinebrook<br>Lyric Opera</div>

    <div class="vertical web-opera">pinebrookvocal.org</div>
    <div class="vertical web-orchestra">thesilvestri.org</div>
    <div class="vertical phone">(860) 472-6081</div>

    <p class="credits credits-cast">
      Rosita : Velda Rose Marsh<br>
      Don Alvar : Bartholomew Fenwick<br>
      Leandro : Dorian Webb<br>
      Inésa : Annelise Krov<br>
      <span class="indent">Joan Pettigrew</span>
    </p>
    <p class="credits credits-team">
      Stage Director, Conductor :<br>
      Marcus Tolvane<br>
      Chorus Master<br>
      Lena Whitmoor
    </p>

    <p class="show show-a">
      <span class="show-date">Fri. November 9</span>
      7:30 pm. New Britain<br>
      Harrow-By-Elm (47 Birch Rd)
    </p>
    <p class="show show-b">
      <span class="show-date">Sun. November 11</span>
      4 pm. New London<br>
      Ossel Arts Center (718 Quill Ave)
    </p>
    <p class="show show-c">
      <span class="show-date">Sat. November 17</span>
      7:30 pm. Middletown<br>
      RQT Performing Arts Center (514 Pellam Ct)
    </p>
    <p class="show show-d">
      <span class="show-date">Sun. November 18</span>
      2 pm. Hartford<br>
      Fairbrook Lyceum<br>
      Museum of Art (283 Cedar Way)
    </p>
  </main>
</body>
</html>
```